2-Page Flyer for the Information Session about the Quiet Venture Pathway

This is a flyer to announce/advertise an evening Information Session about the Quiet Venture Pathway. This Program aims at mindfully rethinking and redesigning work (and life) for people who feel stuck or not entirely satisfied with their work and/or life (please see draft flyer attached for more details). This Program is property of Bright Meadow, a company that uses a combination of Mindfulness, Design, and Entrepreneurship to help people achieve greater happiness (in their work and lives).
Updates

Target Market(s)

People who feel stuck or not entirely satisfied with their work and/or life (please see draft flyer attached for more details)

Font styles to use
Serif
Sans Serif

Colors
ffffff
f37122
33a6d7
acd037

Requirements
Must have
• All of what I will say below is suggestive (I’m not a design expert), and I’m open to divert from it, if it makes sense and feels more interesting.
• I thought initially of a 2-page flyer (please see draft flyer attached). The first page could help people grasp the essence of the event quickly (in 1 or 2 minutes), and then, if they are interested/motivated, they would continue reading through page 2, which has more info about the Program in itself.
• Potential Structure
• Page 1
• . About the Information Session on the Quiet Venture Pathway
• . Visible Date & Time, Contacts, Venue (and other relevant info)
• . About me (the facilitator)
• Page 2
• . About the Quiet Venture Pathway
• I include a Powerpoint draft of the flyer with the content. The design is rudimentary and precarious from an aesthetics/organization point of view, and this is mainly where I need help (and maybe in other aspects too!).
• On the flyer, I would like to include:
• . A photo of myself (I attach 1 picture).
• . 1 or 2 beautiful-nature photos (cropped or full). One may have to do with looking at the sky, dreaming, and imagining a new work and life (2 photos with sky and clouds attached). The other has to do with walking the transformation journey (the photo with the person walking through the forest path).
• . bright meadow logo or logos (there are two slightly different ones, that can be used for different purposes). For the first page, I would like the bright meadow logo that has "bright meadow" written on the bottom, with the saying "Calm, Craft and Enterprise for Joyful Living" beneath. This is the main logo. For the 2nd page, you can choose the logo that adapts better.
• - Where it says the "the way out is in" it would be great to have a similar font to the one I attach (see file "Font_the_way_out_is_in.png" and Torvenscript-qr.ttf
Nice to have
• In terms of colours, I would not divert much from the logo colours (and of course white and black). I would like the flyer to be quite white. Almost like fairy-tale white: the white horse, the white snow, the white of the stars, the white heaven. White could be the base colour. White means peace, tranquillity, calm contentment, a smile.
• And then use the other colours. The green of the mindfulness. The blue of the sky, the dreams. And the orange of the sun, the energy, the fire, the action. And maybe the black for text.
• Where it says the "the way out is in" it would be great to have a similar font to the one I attach (see file "Font_the_way_out_is_in".
• I would like this flyer to be a piece of art, in every possible way. Simple, beautiful, ease, light, peaceful, calm happy. Just like the Quiet Venture Pathway and bright meadow Company that I am creating intends to be. The mission of this Program and Company is to be a designer, a painter (a Picasso) of happier and more fulfilling human lives.
• I am very much looking forward to seeing your proposal(s).

```html
<!DOCTYPE html>
<html lang="en">
<head>
<meta charset="utf-8">
<title>Quiet Venture Pathway – Information Session Flyer</title>
<link rel="stylesheet" href="https://fonts.googleapis.com/css2?family=Caveat:wght@600&family=Open+Sans:ital,wght@0,300;0,400;0,600;0,700;1,400;1,600;1,700&family=Oswald:wght@400;500;700&display=swap">
<style>
:root{
  --white:#ffffff;
  --orange:#f37122;
  --blue:#33a6d7;
  --green:#acd037;
  --ink:#2b2b2b;
  --grey:#9a9a9a;
  --stage:#d9d9d9;
  --sans:"Open Sans",Arial,sans-serif;
  --cond:"Oswald","Arial Narrow",sans-serif;
  --script:"Caveat",cursive;
}
*{box-sizing:border-box;margin:0;padding:0}
html,body{width:1200px;height:808px;overflow:hidden}
body{background:var(--stage);font-family:var(--sans);color:var(--ink);position:relative}
.page{position:absolute;top:71px;width:494px;height:696px;background:var(--white);overflow:hidden}
.page--front{left:81px}
.page--back{left:626px}
.abs{position:absolute}

/* FRONT */
.side-band{left:0;top:0;width:66px;height:696px;background:var(--green);border-radius:0 34px 34px 0}
.side-band__text{position:absolute;left:33px;top:350px;transform:translate(-50%,-50%) rotate(-90deg);white-space:nowrap;color:var(--white);font-weight:300;font-size:29px;letter-spacing:14px}
.hero{left:66px;top:0;width:428px;height:328px;background:linear-gradient(180deg,#8fc3e6 0%,#cfe4f1 35%,#eef4f7 52%,#9fb6c8 70%,#5f7d96 80%)}
.hero__date{left:66px;top:256px;width:428px;height:72px;background:rgba(32,44,56,.82);color:var(--white);text-align:center}
.hero__day{font-weight:300;font-size:19px;margin-top:7px;letter-spacing:-.3px}
.hero__day b{font-weight:700}
.hero__time{font-weight:300;font-size:18px;line-height:20px}
.hero__venue{font-size:11px;font-weight:600;margin-top:4px}
.hero__venue span{color:var(--green)}
.brand{display:flex;align-items:center;gap:6px;white-space:nowrap}
.brand__dot{width:14px;height:14px;border-radius:50%;background:var(--orange)}
.brand__name{font-family:var(--sans);font-weight:400;color:var(--blue)}
.front-brand{left:66px;width:428px;top:88px;justify-content:center}
.front-brand .brand__name{font-size:24px}
.tagline{left:66px;width:428px;top:123px;text-align:center;font-style:italic;font-size:8.6px}
.title{left:66px;width:428px;text-align:center;font-family:var(--cond);font-weight:700;line-height:1;letter-spacing:-.5px}
.title--a{top:138px;font-size:38px;color:var(--green)}
.title--b{top:176px;font-size:40px;color:#222}
.title--c{top:214px;font-size:38px;color:var(--white)}
.copy{font-size:9.2px;line-height:11px;text-align:justify}
.intro{left:82px;top:337px;width:388px}
.section-head{font-weight:700;font-size:14px;color:var(--green);letter-spacing:.2px}
.who{left:82px;top:374px;width:388px;display:flex;align-items:center;gap:12px}
.who i{flex:1;height:1.5px;background:var(--green)}
.who-copy{left:82px;top:393px;width:388px}
.facilitator{left:81px;top:448px;width:118px;height:162px;background:var(--white);box-shadow:0 0 3px rgba(0,0,0,.18);padding:6px}
.facilitator__label{font-size:11px;letter-spacing:3px;color:#a8a8a8;text-align:center}
.facilitator__photo{margin-top:7px;width:106px;height:128px;background:linear-gradient(160deg,#e4e4e4,#bdbdbd 55%,#5a6470)}
.bio-name{left:212px;top:446px;font-weight:700;font-size:15px}
.bio-role{left:212px;top:468px;font-size:7px;font-style:italic;font-weight:700;color:var(--orange)}
.bio{left:212px;top:480px;width:258px;font-size:7.6px;line-height:9.9px;text-align:justify}
.booking-tab{height:24px;color:var(--white);font-weight:700;font-style:italic;font-size:15px;display:flex;align-items:center;white-space:nowrap}
.front-tab{left:66px;top:621px;width:245px;background:var(--blue);border-radius:0 14px 14px 0;padding-left:14px}
.contact{display:flex;align-items:center;gap:6px;white-space:nowrap}
.contact__phone{font-family:var(--cond);font-weight:500;font-size:25px;color:#222;letter-spacing:-.3px}
.contact__mail{font-size:15px;color:#222;letter-spacing:-.4px}
.front-phone{left:82px;top:648px}
.front-mail{left:281px;top:655px}
.front-mail .contact__mail{margin-left:5px}

/* BACK */
.back-sky{left:0;top:0;width:494px;height:82px;background:linear-gradient(180deg,#b9d7ec,#e3eef6 70%,#f4f8fb)}
.back-title{left:25px;top:18px;font-weight:700;font-style:italic;font-size:15px;color:var(--orange)}
.back-lead{left:25px;top:41px;width:447px;font-size:8.4px;line-height:10.8px;font-style:italic}
.tab{height:20px;color:var(--white);font-weight:700;font-size:13px;display:flex;align-items:center;padding-left:24px;border-radius:0 12px 12px 0}
.tab--program{left:0;top:98px;width:137px;background:var(--orange)}
.tab--why{left:0;top:290px;width:80px;background:var(--blue)}
.tab--how{left:245px;top:290px;width:68px;background:var(--green);padding-left:14px}
.how-rule{left:245px;top:290px;width:1.5px;height:205px;background:var(--green)}
.program-copy{left:25px;top:131px;width:206px;font-size:8.5px;line-height:10.9px}
.program-copy p+p{margin-top:10px}
.cycle{left:235px;top:90px;width:259px;height:200px;overflow:visible}
.why-copy{left:25px;top:326px;width:206px;font-size:8.5px;line-height:10.8px}
.how-copy{left:260px;top:326px;width:215px;font-size:8.5px;line-height:10.8px}
.list{list-style:none;margin-top:6px}
.list li{position:relative;padding-left:14px;margin-bottom:6px}
.list li::before{content:attr(data-n);position:absolute;left:0;top:1px;width:9px;height:9px;border-radius:50%;background:var(--green);color:var(--white);font-size:6.5px;font-weight:700;text-align:center;line-height:9px}
.forest{left:0;top:499px;width:494px;height:116px;background:linear-gradient(90deg,#2a2a18,#4a4628 35%,#7d7044 52%,#44402a 72%,#262616);border-radius:0 0 0 30px}
.quote{left:62px;top:514px;font-family:var(--script);font-weight:600;font-size:54px;line-height:1;color:var(--white);white-space:nowrap;letter-spacing:.5px}
.quote-by{left:290px;top:578px;font-size:9.5px;font-style:italic;color:var(--orange);white-space:nowrap}
.back-tab{left:133px;top:614px;width:361px;height:28px;background:var(--orange);border-radius:18px 0 0 0;justify-content:center}
.back-brand{left:22px;top:668px}
.back-brand .brand__name{font-size:15px}
.back-phone{left:145px;top:652px}
.back-phone .contact__phone{font-size:22px}
.back-mail{left:305px;top:658px}
.back-mail .contact__mail{font-size:14px;margin-left:4px}
</style>
</head>
<body>

<section class="page page--front" aria-label="Front page">
  <div class="abs side-band"><span class="side-band__text">INFORMATION SESSION</span></div>
  <div class="abs hero" role="img" aria-label="Photo of a bright cloudy sky above distant mountain ridges"></div>

  <div class="abs brand front-brand"><span class="brand__dot"></span><span class="brand__name">bright meadow</span></div>
  <p class="abs tagline">Calm, Craft and Enterprise for Joyful Living</p>

  <h1>
    <span class="abs title title--a">QUIET</span>
    <span class="abs title title--b">VENTURE</span>
    <span class="abs title title--c">PATHWAY</span>
  </h1>

  <div class="abs hero__date">
    <p class="hero__day">Thursday <b>5th September 2019</b></p>
    <p class="hero__time">19:30 to 21:00</p>
    <p class="hero__venue"><span>Venue:</span> Lantern Coworking, C/ Verdera 14, Barcelona</p>
  </div>

  <p class="abs copy intro">The purpose of this <b>free Information Session</b> is to give you a real insight into the <b>Quiet Venture Pathway</b> and how it can help you make the most of your professional and personal life.</p>

  <div class="abs who"><h2 class="section-head">WHO CAN COME</h2><i></i></div>
  <p class="abs copy who-copy">Whether you come on your own, or with friends or family, you’ll be warmly welcomed. The session will take place on Thursday the 5th September 2019, from 19:30 to 21:00, at Lantern Coworking. Please see information below to get in contact or to book a seat.</p>

  <div class="abs facilitator">
    <p class="facilitator__label">FACILITATOR</p>
    <div class="facilitator__photo" role="img" aria-label="Portrait photo of the facilitator"></div>
  </div>
  <h3 class="abs bio-name">Dr Marco Elvane</h3>
  <p class="abs bio-role">Visiting Research Fellow, Westbrook University</p>
  <p class="abs bio">Marco joined the Westbrook University School of Management as a Lecturer in Entrepreneurship in 2015. He completed his PhD in Entrepreneurship at Kelmore Business School in 2014, receiving the prestigious Institute of Management’s Hartwell Doctoral Dissertation Award. He began his business career as a Production Engineer for Voltaris, and later as a Sales Engineer for Norvance. After his MBA, he served as a Strategy Consultant for Dourada Business School. Originally from Portugal, Marco enjoys designing and launching new ideas, international communities, mindfulness retreats, and musical improvisation. He nurtures a close connection to Still Pines Mindfulness Centre, where he has practiced and volunteered over 9 months. He has a broad experience of sharing the benefits of mindfulness with others.</p>

  <div class="abs booking-tab front-tab">Information &amp; Booking</div>
  <div class="abs contact front-phone">
    <svg width="9" height="20" viewBox="0 0 9 20" aria-hidden="true"><path d="M7 1 C2 3 1 8 1 10 C1 12 2 17 7 19" fill="none" stroke="var(--blue)" stroke-width="3" stroke-linecap="round"/></svg>
    <span class="contact__phone">+34 600 555 019</span>
  </div>
  <div class="abs contact front-mail">
    <svg width="18" height="13" viewBox="0 0 18 13" aria-hidden="true"><rect x="1" y="1" width="16" height="11" fill="none" stroke="var(--blue)" stroke-width="1.6"/><path d="M1 1 L9 8 L17 1" fill="none" stroke="var(--blue)" stroke-width="1.6"/></svg>
    <span class="contact__mail">info@brightmeadow.io</span>
  </div>
</section>

<section class="page page--back" aria-label="Back page">
  <div class="abs back-sky" role="img" aria-label="Soft photo of pale sky and clouds"></div>
  <h2 class="abs back-title">What is Quiet Venture</h2>
  <p class="abs back-lead">Being mindful means being aware and awake. Entrepreneurship is the creation of a new form of organising. Quiet Venture is then the process of creating or redesigning your work and life with awareness, in a way that is reflective of you, of your passions and values, thus conducing to a greater sense of fulfilment and happiness.</p>

  <div class="abs tab tab--program">THE PROGRAM</div>
  <div class="abs program-copy">
    <p style="text-align:justify"><b>The Quiet Venture Pathway</b> is a <b>4-month long transformative journey</b> designed for people who feel stuck or not entirely satisfied with their professional and/or personal life. It will be of benefit for everyone, at any stage.</p>
    <p style="text-align:justify">The Program consists of a 5-hour workshop every month, complemented by 2-hour weekly peer support meetings. It combines mindfulness techniques, design thinking methodology, and entrepreneurship frameworks.</p>
  </div>

  <svg class="abs cycle" viewBox="0 0 259 200" aria-label="Program cycle of four workshops linked by weekly peer support meetings" font-family="Open Sans, sans-serif">
    <defs><marker id="tip" markerWidth="6" markerHeight="6" refX="3" refY="3" orient="auto"><path d="M0 0 L6 3 L0 6 Z" fill="context-stroke"/></marker></defs>
    <path d="M68 58 Q72 46 84 42" fill="none" stroke="#8a8a8a" stroke-width="3" marker-end="url(#tip)"/>
    <path d="M152 52 Q164 56 168 66" fill="none" stroke="var(--green)" stroke-width="3" marker-end="url(#tip)"/>
    <path d="M168 128 Q168 142 158 146" fill="none" stroke="var(--blue)" stroke-width="3" marker-end="url(#tip)"/>
    <path d="M84 150 Q72 146 70 134" fill="none" stroke="var(--orange)" stroke-width="3" marker-end="url(#tip)"/>
    <g text-anchor="middle" fill="#fff">
      <circle cx="117" cy="37" r="34" fill="var(--green)"/>
      <text x="117" y="38" font-size="7">Workshop 1</text><text x="117" y="48" font-size="8" font-weight="700">INSIGHT</text><text x="117" y="57" font-size="7">(5 hours)</text>
      <circle cx="190" cy="97" r="34" fill="var(--blue)"/>
      <text x="190" y="98" font-size="7">Workshop 2</text><text x="190" y="108" font-size="8" font-weight="700">DESIGN</text><text x="190" y="117" font-size="7">(5 hours)</text>
      <circle cx="117" cy="157" r="34" fill="var(--orange)"/>
      <text x="117" y="158" font-size="7">Workshop 3</text><text x="117" y="168" font-size="8" font-weight="700">EXECUTE</text><text x="117" y="177" font-size="7">(5 hours)</text>
      <circle cx="49" cy="97" r="34" fill="#c4c4c4"/>
      <text x="49" y="98" font-size="7">Workshop 4</text><text x="49" y="108" font-size="8" font-weight="700">PRESENT</text><text x="49" y="117" font-size="7">(5 hours)</text>
    </g>
    <g font-size="6.5" font-style="italic">
      <text x="12" y="47" fill="#a0a0a0">WPS meetings</text>
      <g text-anchor="middle" fill="var(--green)">
        <text x="203" y="34">Weekly Peer Support</text>
        <text x="203" y="42">(WPS) meetings</text>
        <text x="203" y="50">(2 hours)</text>
      </g>
      <text x="171" y="155" fill="var(--blue)">WPS meetings</text>
      <text x="21" y="153" fill="var(--orange)">WPS meetings</text>
    </g>
  </svg>

  <div class="abs tab tab--why">WHY</div>
  <div class="abs how-rule"></div>
  <div class="abs tab tab--how">HOW</div>

  <div class="abs why-copy">
    <p style="text-align:justify">Many people are not satisfied with their work or life, but they don’t know what to do about it. This Program offers you a safe place to conduct your inner journey with collective support, helping you reflect, design, and (very likely) do something about it. It aims at:</p>
    <ul class="list">
      <li data-n="1">Increasing awareness, clarity and confidence</li>
      <li data-n="2">Having a deeper <b><i>insight</i></b> on what makes you happier and what you want</li>
      <li data-n="3">Developing a clear <b><i>design</i></b> integrating your intended work and life</li>
      <li data-n="4">Start <b><i>executing</i></b> this design.</li>
    </ul>
  </div>
  <div class="abs how-copy">
    <p>This Program differs from existing entrepreneurial programs in many ways:</p>
    <ul class="list">
      <li data-n="1">Uses mindfulness and self analysis to look deeply into yourself</li>
      <li data-n="2">Design and execution decisions are based on happiness rather than (only) financials</li>
      <li data-n="3">Holistic and inclusive design process, integrating work and life, and building synergies between your different parts.</li>
    </ul>
    <p>The Program format includes lectures, individual work, group sharing, guided activities, experiential exercises, video, audio, handouts and other resources.</p>
  </div>

  <div class="abs forest" role="img" aria-label="Photo of a person walking a forest path between tall trees"></div>
  <p class="abs quote">the way out is in</p>
  <p class="abs quote-by">Zen Master Tien Minh An</p>

  <div class="abs booking-tab back-tab">Information &amp; Booking</div>
  <div class="abs brand back-brand"><span class="brand__dot"></span><span class="brand__name">bright meadow</span></div>
  <div class="abs contact back-phone">
    <svg width="8" height="18" viewBox="0 0 9 20" aria-hidden="true"><path d="M7 1 C2 3 1 8 1 10 C1 12 2 17 7 19" fill="none" stroke="var(--orange)" stroke-width="3" stroke-linecap="round"/></svg>
    <span class="contact__phone">+34 600 555 019</span>
  </div>
  <div class="abs contact back-mail">
    <svg width="16" height="12" viewBox="0 0 18 13" aria-hidden="true"><rect x="1" y="1" width="16" height="11" fill="none" stroke="var(--orange)" stroke-width="1.6"/><path d="M1 1 L9 8 L17 1" fill="none" stroke="var(--orange)" stroke-width="1.6"/></svg>
    <span class="contact__mail">info@brightmeadow.io</span>
  </div>
</section>

</body>
</html>
```